Brochure needed for 3D foam prop company

Looking for a designer to create a multi page brochure. Brochure will need to be able to be die cut so we're looking for something unique. The brochure needs to utilize our logo and the squares as possibly cut aways displaying imagery behind it for the front cover.

The brochure will feature the following sections:
- about us
- our process
- amazing clients
- anything is possible

So far we're still looking for an effective design that matches our requirements. It appears the die cutting element isn't being factored into the design (all except 1 design submitted has included this so far). Please read the brief and submit quality designs...so far we have not been very impressed.

Target Market(s)

Themeparks, water parks

Industry/Entity Type

Entertainment Industry

Font styles to use
Sans Serif

Requirements
Must have
• Logo, utilize our color theme

```html
<!DOCTYPE html>
<html lang="en">
<head>
<meta charset="utf-8">
<title>Apex Foam Brochure Spreads</title>
<link href="https://fonts.googleapis.com/css2?family=Didact+Gothic&display=swap" rel="stylesheet">
<style>
:root{
  --blue:#0a6ec0;
  --orange:#f7941d;
  --yellow:#f2e000;
  --sky:#5ec8f0;
  --backdrop:#c0c1c3;
  --ink:#2b2b2b;
  --muted:#555;
  --paper:#f3f3f4;
  --track:#efefef;
}
*{margin:0;padding:0;box-sizing:border-box}
html,body{width:1200px;height:963px;overflow:hidden;background:var(--backdrop)}
body{font-family:"Didact Gothic",sans-serif;color:var(--ink)}
.stage{position:absolute;left:0;top:0;width:1469px;height:1179px;transform:scale(0.81688,0.81679);transform-origin:0 0}
.page{position:absolute;overflow:hidden}
.abs{position:absolute}
.stripe{position:absolute;height:9px;display:flex}
.stripe span{display:block;height:100%}
.c-blue{background:var(--blue)}.c-orange{background:var(--orange)}.c-yellow{background:var(--yellow)}.c-sky{background:var(--sky)}
.heading-orange{color:var(--orange);font-size:23px;font-weight:400}
.body-copy{font-size:11px;line-height:13.4px}
/* about */
.about{left:61px;top:50px;width:679px;height:525px;background:linear-gradient(90deg,#fff 0%,#fff 40%,#e6e7e9 100%)}
.mission-title{color:var(--blue)}
.tools-box{left:62px;top:355px;width:548px;height:83px;background:var(--orange);color:#fff;text-align:center;font-size:11px;line-height:14px;padding-top:14px;z-index:2}
.pride-band{left:0;top:427px;width:679px;height:88px;background:var(--blue);color:#fff;font-size:18px;text-align:center;padding-top:34px}
/* capabilities */
.capabilities{left:740px;top:50px;width:678px;height:525px;background:linear-gradient(180deg,#fafafa,#e9eaeb)}
.thrive-band{left:0;top:10px;width:678px;height:87px;background:var(--blue);color:#fff;font-size:16px;padding:36px 0 0 80px}
.feature{width:200px;text-align:center}
.feature svg{display:block;margin:0 auto}
.feature h3{color:var(--blue);font-size:10px;font-weight:400;margin-top:12px;letter-spacing:.2px}
.feature p{font-size:10px;line-height:12.5px;color:var(--muted);margin-top:12px}
/* process */
.process{left:61px;top:618px;width:679px;height:524px;background:#fff}
.city-band{left:0;width:679px;background:linear-gradient(180deg,#5d93c2,#6a9dc8 60%,#5b8dbb)}
.process-title{color:#fff;font-size:22px;left:52px;top:46px}
.step{width:118px;text-align:center}
.step h3{color:var(--blue);font-size:11px;font-weight:400;margin-top:20px;line-height:13px}
.step p{font-size:9px;line-height:11.3px;color:#222;margin-top:10px}
.process-note{color:#fff;font-size:12px;line-height:14.5px;text-align:center;left:70px;width:540px;top:16px}
/* why choose */
.why{left:740px;top:618px;width:678px;height:524px;background:linear-gradient(180deg,#f7f7f7,#eeeeef)}
.reasons{left:80px;top:94px;width:480px;list-style:none}
.reasons li{position:relative;padding-left:22px;font-size:11px;line-height:13.4px;margin-bottom:13.6px}
.reasons svg{position:absolute;left:0;top:1px}
.member{font-size:11px;line-height:13.4px;width:160px}
.member-badge{display:block}
</style>
</head>
<body>
<div class="stage">

  <!-- About spread page -->
  <section class="page about">
    <div class="stripe" style="left:0;top:0;width:679px"><span class="c-blue" style="width:520px"></span><span class="c-yellow" style="width:53px"></span><span class="c-sky" style="width:52px"></span><span class="c-orange" style="width:54px"></span></div>
    <h1 class="abs heading-orange" style="left:63px;top:46px">About Us</h1>
    <p class="abs body-copy" style="left:64px;top:95px;width:236px">Our team of fabricators, design strategists, concept artists, high tech machinery, and top of the line materials, work to deliver foam props for companies big and small, start-ups or stalwarts. We don’t just come up with what’s cool; we craft items that your customers want to see and ones that make you look great. We’ve seen first hand how the power of foam props can elevate a company from not being noticed to top of the list; how it can rescue a business from the trenches of an impossible-to-win price war with competitors, and how it can motivate employees and customers alike to become full-fledged fans.<br><br>We develop the props that get you noticed.</p>
    <div class="abs body-copy" style="left:365px;top:95px;width:262px">
      <p class="mission-title">Our Company Mission</p>
      <p>At Apex Foam, we believe there is an intrinsic value, personal reward and financial reward in offering cost-effective solutions and reliable products that offer our clients more value than they expect to receive. We, meaning each employee of Apex, succeeds because our customers succeed. We act responsibly when we help protect our environment, provide economic opportunity fairly, work safely, and consider all employees in all of our business affairs. Our central focus is the production of EPS (Expanded Polystyrene) foam-based products including custom 3D company signs, aerospace prototypes and products, haunt industry products, themed attractions, movie and tv show props, and much more.</p>
    </div>
    <div class="abs pride-band">We Pride Ourselves On Creativity, Intuition &amp; Determination.</div>
    <div class="abs tools-box">The Right Tools. The Right Solution.<br><br>We use world class artists, state of the art 3D Scanners, CNC Machines, and Hot Wire<br>Cutters to deliver out of this world props based on your specifications.</div>
    <div class="abs" style="left:0;top:515px;width:679px;height:10px;background:#fff"></div>
  </section>

  <!-- Capabilities page -->
  <section class="page capabilities">
    <div class="abs" style="left:0;top:0;width:678px;height:10px;background:#e8e8e8"></div>
    <div class="abs thrive-band">We Thrive On Challenging Projects. They Produce Bigger Rewards In The End.</div>

    <div class="abs feature" style="left:78px;top:144px">
      <svg width="36" height="36" viewBox="0 0 36 36"><circle cx="18" cy="18" r="17" fill="#fff" stroke="#0a6ec0" stroke-width="1.3"/><g fill="#0a6ec0"><rect x="11" y="11" width="4" height="4"/><rect x="16" y="11" width="4" height="4"/><rect x="21" y="11" width="4" height="4"/><rect x="11" y="16" width="4" height="4"/><rect x="16" y="16" width="4" height="4"/><rect x="21" y="16" width="4" height="4"/><rect x="11" y="21" width="4" height="4"/><rect x="16" y="21" width="4" height="4"/><rect x="21" y="21" width="4" height="4"/></g></svg>
      <h3>Concept Art &amp; Modeling</h3>
      <p>Let our talented team of artists take your idea and turn it into reality using professional techniques and industry standard software</p>
    </div>
    <div class="abs feature" style="left:379px;top:144px">
      <svg width="36" height="36" viewBox="0 0 36 36"><circle cx="18" cy="18" r="17" fill="#fff" stroke="#0a6ec0" stroke-width="1.3"/><g fill="none" stroke="#0a6ec0" stroke-width="1.4"><rect x="11" y="12" width="14" height="11"/><path d="M9 10h4v4H9zM23 10h4v4h-4zM9 21h4v4H9zM23 21h4v4h-4z"/></g></svg>
      <h3>3D Scanning and Scaleability</h3>
      <p>We utilize a 3D laser scanning system for creating perfect 3D digital copies of virtually any physical object. Once scanned, the objects can be scaled or modified.</p>
    </div>
    <div class="abs feature" style="left:85px;top:321px">
      <svg width="36" height="36" viewBox="0 0 36 36"><circle cx="18" cy="18" r="17" fill="#fff" stroke="#0a6ec0" stroke-width="1.3"/><path fill="#0a6ec0" d="M12 15h4v-3h4v3h4v4h-2v5h-5v-3h-2v3h-3z"/></svg>
      <h3>Innovative Hot Wire Cutters</h3>
      <p>Boasting industrial strength construction along with top of the line speed and accuracy and capable of 2D, flat, spiral and lathe cuts, our Hot Wire Cutters are a path to improved quality.</p>
    </div>
    <div class="abs feature" style="left:381px;top:315px">
      <svg width="36" height="36" viewBox="0 0 36 36"><circle cx="18" cy="18" r="17" fill="#fff" stroke="#0a6ec0" stroke-width="1.3"/><path fill="#0a6ec0" d="M12 10h9l4 4v13H12z"/><rect x="15" y="16" width="7" height="7" fill="#fff"/></svg>
      <h3>Fast CNC Machine</h3>
      <p>Our 4 Axis CNC Foam Router allows us to create pieces up to 4ft diameter and 8ft length in one run. Create larger and more intricate pieces than ever before.</p>
    </div>

    <div class="stripe" style="left:0;top:515px;width:678px;height:10px"><span class="c-orange" style="width:53px"></span><span class="c-sky" style="width:52px"></span><span class="c-yellow" style="width:52px"></span><span class="c-blue" style="width:521px"></span></div>
  </section>

  <!-- Process page -->
  <section class="page process">
    <div class="stripe" style="left:0;top:0;width:679px"><span class="c-blue" style="width:520px"></span><span class="c-yellow" style="width:53px"></span><span class="c-sky" style="width:52px"></span><span class="c-orange" style="width:54px"></span></div>
    <div class="abs city-band" style="top:9px;height:81px" role="img" aria-label="Blue-tinted city skyline photograph"></div>
    <h2 class="abs process-title">Our Proven Process, Produces Results</h2>

    <svg class="abs" style="left:0;top:120px" width="679" height="110" viewBox="0 0 679 110">
      <g fill="none" stroke-width="4">
        <circle cx="94" cy="55" r="46" stroke="var(--track)"/>
        <path d="M94 9 A46 46 0 0 1 139 45" stroke="#5a8fc4"/>
        <circle cx="215" cy="55" r="46" stroke="var(--track)"/>
        <path d="M215 9 A46 46 0 0 1 230 98" stroke="#d3a75f"/>
        <circle cx="335" cy="55" r="46" stroke="var(--track)"/>
        <path d="M335 9 A46 46 0 1 1 304 89" stroke="#b5c58a"/>
        <circle cx="456" cy="55" r="46" stroke="var(--track)"/>
        <path d="M456 9 A46 46 0 1 1 412 42" stroke="#c8643a"/>
        <circle cx="576" cy="55" r="46" stroke="#000"/>
      </g>
      <g>
        <path d="M88 50h12v7h-7l-4 3v-3h-1z" fill="none" stroke="#5a8fc4" stroke-width="1.5"/>
        <rect x="205" y="47" width="20" height="15" fill="#d3a75f"/><path d="M207 60l5-6 4 4 3-3 4 5z" fill="#fff"/>
        <g fill="#b5c58a"><rect x="326" y="50" width="8" height="8"/><rect x="336" y="50" width="8" height="8"/><rect x="331" y="43" width="8" height="8"/></g>
        <rect x="450" y="45" width="12" height="19" fill="#d3a75f"/>
        <path d="M569 58l6-4-2-6 2-1 4 6 5-2 1 2-5 3 2 6-2 1-3-6-6 3z" fill="#000"/>
      </g>
    </svg>

    <div class="abs step" style="left:35px;top:247px"><h3>DISCOVERY</h3><p>We learn about your project’s goals and work with you to determine what will set you apart from your competition.</p></div>
    <div class="abs step" style="left:156px;top:247px"><h3>CONCEPT</h3><p>Working with our amazing team of world class concept artists, we’ll develop concepts that will get your heart pumping and get you excited about what the final product will ultimately look like.</p></div>
    <div class="abs step" style="left:276px;top:247px"><h3>MODELING</h3><p>As your project moves into the modeling phase, this is where your concept turns into something amazing. Our state of the art machines take over at this stage.</p></div>
    <div class="abs step" style="left:397px;top:247px"><h3>CARVING</h3><p>This is where your prop design meets the titanium drill bit so we say! Your 3D model is sent to our on-site Hot Wire Cutter and CNC Machines to produce your masterpiece.</p></div>
    <div class="abs step" style="left:517px;top:247px"><h3>PAINTING +<br>DELIVERY</h3><p>Once your project is in this phase we will paint the product based on your specifications and prepare the order for shipping and final delivery.</p></div>

    <div class="abs city-band" style="top:420px;height:104px" role="img" aria-label="Blue-tinted city skyline photograph"></div>
    <p class="abs process-note" style="top:436px">From Concept to clear coated, almost indestructible prop, our process starts by giving you freedom to unleash your imagination. We’ll work on an amazing concept, move to modeling, foam mill cutting and more.</p>
  </section>

  <!-- Why choose page -->
  <section class="page why">
    <h2 class="abs heading-orange" style="left:70px;top:45px;font-size:22px">Why Choose Us</h2>
    <ul class="abs reasons">
      <li><svg width="11" height="11" viewBox="0 0 11 11"><circle cx="5.5" cy="5.5" r="4.8" fill="none" stroke="#3aa0dc"/><path d="M3 5.5l2 2 4-4" fill="none" stroke="#3aa0dc" stroke-width="1.3"/></svg>Very responsive and quick turnaround times on artwork</li>
      <li><svg width="11" height="11" viewBox="0 0 11 11"><circle cx="5.5" cy="5.5" r="4.8" fill="none" stroke="#3aa0dc"/><path d="M3 5.5l2 2 4-4" fill="none" stroke="#3aa0dc" stroke-width="1.3"/></svg>State of the art machinery to cut down on production times</li>
      <li><svg width="11" height="11" viewBox="0 0 11 11"><circle cx="5.5" cy="5.5" r="4.8" fill="none" stroke="#3aa0dc"/><path d="M3 5.5l2 2 4-4" fill="none" stroke="#3aa0dc" stroke-width="1.3"/></svg>Experienced and talented team of artists and fabricators</li>
      <li><svg width="11" height="11" viewBox="0 0 11 11"><circle cx="5.5" cy="5.5" r="4.8" fill="none" stroke="#3aa0dc"/><path d="M3 5.5l2 2 4-4" fill="none" stroke="#3aa0dc" stroke-width="1.3"/></svg>Multiple industries served including aerospace, b2b, prototyping, movies and tv, art, architecture, family entertainment centers and amusement parks, festivals, music fests, beer fests, surfboard and boogie board blanks, construction, and much more</li>
      <li><svg width="11" height="11" viewBox="0 0 11 11"><circle cx="5.5" cy="5.5" r="4.8" fill="none" stroke="#3aa0dc"/><path d="M3 5.5l2 2 4-4" fill="none" stroke="#3aa0dc" stroke-width="1.3"/></svg>Amazing support because we care about your project as much as you do</li>
    </ul>
    <h2 class="abs heading-orange" style="left:70px;top:305px;font-size:22px">Proud Members</h2>
    <p class="abs member" style="left:70px;top:352px">Proud Members of the Global Guild of Amusement Venues and Attractions</p>
    <p class="abs member" style="left:253px;top:352px">Proud Members of the Themed Attractions Alliance</p>
    <p class="abs member" style="left:438px;top:352px;width:170px">Proud Members of the Aquatic Parks Council</p>
    <svg class="abs member-badge" style="left:110px;top:410px" width="56" height="56"><circle cx="28" cy="28" r="24" fill="#6b2b8c"/></svg>
    <svg class="abs member-badge" style="left:295px;top:410px" width="56" height="56"><rect x="6" y="6" width="44" height="44" fill="#1d2f6f"/></svg>
    <svg class="abs member-badge" style="left:485px;top:400px" width="60" height="60"><circle cx="30" cy="30" r="28" fill="#2a82c6"/></svg>
    <div class="stripe" style="left:0;top:515px;width:678px;height:9px"><span class="c-orange" style="width:53px"></span><span class="c-sky" style="width:52px"></span><span class="c-yellow" style="width:52px"></span><span class="c-blue" style="width:521px"></span></div>
  </section>

</div>
</body>
</html>
```